bluecastle aquatics of northeast florida business card

I need a new attractive business card. I am planning on printing on very thick rounded corner stock and having painted edges. We are a swimming pool remodel, repair, and service company in north florida. Our current logo is red, white, and blue. It doesn't necessarily have to stay that way, I am open to other ideas. It will need to contain my name, work and cell numbers, email, website, and my contractor license number.

Target Market(s)

High end residential and commercial clients

Industry/Entity Type

Business

Contact Information for Business Card

Company name, employee name and title, work and cell phone numbers, email and website, and Contractor number.

our work scope should be on card somewhere: remodel ~ repair ~ service

logo or slight variation of logo also. (not necessarily set on keeping exact logo)

Colors

Designer to choose colors to be used in the design.

Requirements
Nice to have
• We deal with water so I think some sort of water element or just a color similar to pool water would be nice to integrate into design.

```html
<!DOCTYPE html>
<html lang="en">
<head>
<meta charset="utf-8">
<title>Bluecastle Aquatics of Northeast Florida – Business Card</title>
<link rel="stylesheet" href="https://fonts.googleapis.com/css2?family=Roboto:wght@400;500;700&family=Roboto+Condensed:wght@500;700&display=swap">
<style>
  :root {
    --backdrop: #2c2c2e;
    --card: #1d1e20;
    --card-edge: #26272a;
    --pool-blue: #1b8fd8;
    --signal-red: #e63a4c;
    --ink-light: #f2f2f2;
    --divider: #9a9a9a;
  }
  * { margin: 0; padding: 0; box-sizing: border-box; }
  html, body {
    width: 1200px;
    height: 900px;
    overflow: hidden;
    background: var(--backdrop);
  }
  .stage {
    width: 1200px;
    height: 900px;
    display: flex;
    flex-direction: column;
    align-items: center;
    justify-content: center;
    gap: 36px;
  }
  .card {
    position: relative;
    width: 620px;
    height: 354px;
    background: var(--card);
    border: 1px solid var(--card-edge);
    border-radius: 14px;
    box-shadow: 0 10px 28px rgba(0,0,0,0.45);
    font-family: "Roboto", Arial, sans-serif;
  }

  /* Front */
  .card-front {
    display: flex;
    flex-direction: column;
    align-items: center;
  }
  .brand {
    margin-top: 92px;
    display: flex;
    align-items: center;
    gap: 12px;
  }
  .brand-dot {
    width: 46px;
    height: 46px;
    border-radius: 50%;
    background: var(--signal-red);
    flex: none;
  }
  .brand-name {
    color: var(--pool-blue);
    font-weight: 700;
    text-transform: uppercase;
    line-height: 1;
  }
  .brand-name .line-main {
    display: block;
    font-size: 30px;
    letter-spacing: 2px;
  }
  .brand-name .line-sub {
    display: block;
    margin-top: 4px;
    font-size: 12px;
    letter-spacing: 3.4px;
    border-bottom: 2px solid var(--pool-blue);
    padding-bottom: 3px;
  }
  .scope {
    margin-top: 74px;
    color: var(--ink-light);
    font-size: 15px;
    letter-spacing: 0.6px;
  }

  /* Back */
  .card-back {
    display: flex;
    align-items: center;
    justify-content: center;
  }
  .person {
    text-align: right;
    padding-right: 34px;
  }
  .person-name {
    font-family: "Roboto Condensed", "Arial Narrow", sans-serif;
    font-weight: 700;
    font-size: 34px;
    color: var(--pool-blue);
    text-transform: uppercase;
    line-height: 1.05;
  }
  .person-title {
    font-family: "Roboto Condensed", "Arial Narrow", sans-serif;
    font-weight: 500;
    font-size: 16px;
    color: var(--signal-red);
    text-transform: uppercase;
    margin-top: 4px;
  }
  .divider {
    width: 2px;
    height: 96px;
    background: linear-gradient(to bottom, transparent, var(--divider) 30%, var(--divider) 70%, transparent);
  }
  .contact {
    list-style: none;
    padding-left: 30px;
    color: var(--ink-light);
    font-size: 16px;
    font-weight: 500;
  }
  .contact li {
    display: flex;
    align-items: center;
    gap: 10px;
    line-height: 24px;
  }
  .contact .icon {
    width: 16px;
    height: 16px;
    flex: none;
    fill: var(--pool-blue);
  }
  .contact .license { margin-left: -12px; }
</style>
</head>
<body>
<main class="stage">
  <section class="card card-front">
    <div class="brand">
      <span class="brand-dot"></span>
      <div class="brand-name">
        <span class="line-main">Bluecastle Aquatics</span>
        <span class="line-sub">of Northeast Florida</span>
      </div>
    </div>
    <p class="scope">Remodel . Repair . Service</p>
  </section>

  <section class="card card-back">
    <div class="person">
      <p class="person-name">Evan Marlow</p>
      <p class="person-title">CEO/Founder</p>
    </div>
    <span class="divider"></span>
    <ul class="contact">
      <li>
        <svg class="icon" viewBox="0 0 16 16" aria-hidden="true"><path d="M4.5 1h7a1 1 0 0 1 1 1v12a1 1 0 0 1-1 1h-7a1 1 0 0 1-1-1V2a1 1 0 0 1 1-1zm.5 2v9h6V3H5zm3 10a.8.8 0 1 0 0 1.6.8.8 0 0 0 0-1.6z"/></svg>
        904 555 0187
      </li>
      <li>
        <svg class="icon" viewBox="0 0 16 16" aria-hidden="true"><path d="M1 3.5h14v9H1z M1.5 4 8 9l6.5-5" fill-rule="evenodd"/><path d="M1 4l7 5.2L15 4v8.5H1z"/></svg>
        evan@bluecastleaq.com
      </li>
      <li>
        <svg class="icon" viewBox="0 0 16 16" aria-hidden="true"><circle cx="8" cy="8" r="7"/><path d="M1 8h14M8 1c2.2 2 2.2 12 0 14M8 1c-2.2 2-2.2 12 0 14" stroke="#1d1e20" stroke-width="1.1" fill="none"/></svg>
        www.bluecastleaq.com
      </li>
      <li class="license">Lic no. 40317</li>
    </ul>
  </section>
</main>
</body>
</html>
```